Luxury Wine Label for New Startup Winery

We need a wine label for our new winery startup. We have worked with a local designer but do not feel the resulting label / logo have the elevation required to present our brand as a luxury wine. Our winery is called "Harrowgate Vineyards" and we are focused on extremely high quality hand crafted artisan and estate wines from the Pacific Northwest.
We would like to see designs that utilize a tree line, or other imagery that represents the "Harrowgate" part of our company name. Another interesting feature could be wood grain.
A logo will be required based on your design so please design with this in mind:
This logo should be consistent with the wine bottle label design, and should be representative of our high end exclusive wine while giving a sense of place (Oregon/ Pacific Northwest.)
I will supply an image of the design we received from our local designer, PLEASE NOTE: in general we do like wood grain and tree line concepts but feel the execution was poorly done.
ATTN: Logo design should be suitable for use on: Bottles (Red wine/rose/white wine), Bussiness cards, vehicle signage, business signage, etc
P.S.:
If you have a design that is not outside the box we are still interested in seeing it.
Label is for a burgundy style bottle with a label height of 3.5 - 4" and a width of 3.5-4"
any label <= 4"x4" and >=3.5"x3.5" will be acceptable:
HOWEVER Width should be greater than or equal to height due to the bottle format
Target Market(s)
Wine enthusiasts with adequate discretionary budgets to afford $100 bottles of wine.
Industry/Entity Type
Wine / Winery
Requirements
Must have
- A sense of luxury, a feel of exclusivity, and a theme consistent with our product and brand name
Nice to have
- Tree line, wood grain or other wood themes. Serif fonts
Should not have
- anything cheesy, off topic, hard to read script fonts or anything that makes the label hard to read from a few feet away or too busy

```html
<!DOCTYPE html>
<html lang="en">
<head>
<meta charset="utf-8">
<title>Harrowgate Vineyards – Syrah Label</title>
<link href="https://fonts.googleapis.com/css2?family=Cormorant+Garamond:ital,wght@0,400;1,500&family=Montserrat:wght@500&family=Barlow:wght@600&display=swap" rel="stylesheet">
<style>
  :root {
    --page: #ffffff;
    --label-wine: #2e0309;
    --label-gold: #c4a874;
    --forest-red: #6b0d18;
    --caption-grey: #8a8a8a;
    --bottle-dark: #050102;
    --bottle-glow: #3a0810;
    --capsule-dark: #0e0e0e;
    --capsule-light: #4a4a4a;
    --capsule-band: #8a6d1a;
  }
  * { margin: 0; padding: 0; box-sizing: border-box; }
  html, body { width: 1200px; height: 865px; overflow: hidden; background: var(--page); }
  .presentation { position: relative; width: 1200px; height: 865px; }

  .label {
    position: absolute; width: 397px; height: 397px;
    background: var(--label-wine); overflow: hidden;
  }
  .label--flat { left: 162px; top: 234px; }
  .label__forest {
    position: absolute; left: 0; right: 0; top: 142px; bottom: 0;
    background: linear-gradient(to bottom, rgba(107,13,24,0) 0%, rgba(107,13,24,0.55) 45%, var(--forest-red) 100%);
  }
  .label__frame {
    position: absolute; left: 9px; top: 9px; right: 9px; bottom: 9px;
    border: 3px solid var(--label-gold);
  }
  .label__mark {
    position: absolute; left: 171px; top: 29px; width: 55px; height: 55px;
    border: 1.5px solid var(--label-gold); border-radius: 50%;
  }
  .label__winery {
    position: absolute; left: 0; right: 0; top: 92px; text-align: center;
    font-family: "Cormorant Garamond", serif; font-weight: 400;
    color: var(--label-gold); font-size: 26px; line-height: 25px; letter-spacing: -0.3px;
  }
  .label__varietal {
    position: absolute; left: 0; right: 0; top: 162px; text-align: center;
    font-family: "Cormorant Garamond", serif; font-style: italic; font-weight: 500;
    color: var(--label-gold); font-size: 112px; line-height: 120px;
  }
  .label__vintage, .label__region {
    position: absolute; left: 0; right: 0; text-align: center;
    font-family: "Montserrat", sans-serif; font-weight: 500; color: var(--label-gold);
  }
  .label__vintage { top: 322px; font-size: 17px; letter-spacing: 1.5px; }
  .label__region { top: 352px; font-size: 17px; letter-spacing: 3px; }

  .bottle {
    position: absolute; left: 740px; top: 60px; width: 198px; height: 730px;
  }
  .bottle__art { position: absolute; left: 0; top: 0; }
  .bottle .label {
    left: 10px; top: 434px; transform: scale(0.45); transform-origin: 0 0;
  }

  .caption {
    position: absolute; top: 806px; width: 300px; text-align: center;
    font-family: "Barlow", sans-serif; font-weight: 600; font-size: 17px;
    letter-spacing: 1.6px; color: var(--caption-grey);
  }
  .caption--label { left: 204px; }
  .caption--bottle { left: 690px; }
</style>
</head>
<body>
<main class="presentation">

  <section class="label label--flat">
    <div class="label__forest" role="img" aria-label="Engraved tree line of dark red firs over rolling hills"></div>
    <div class="label__frame"></div>
    <div class="label__mark"></div>
    <p class="label__winery">HARROWGATE<br>VINEYARDS</p>
    <p class="label__varietal">Syrah</p>
    <p class="label__vintage">2024</p>
    <p class="label__region">WILLAMETTE VALLEY</p>
  </section>

  <div class="bottle">
    <svg class="bottle__art" width="198" height="730" viewBox="0 0 198 730" role="img" aria-label="Dark burgundy-style wine bottle with black capsule">
      <defs>
        <linearGradient id="glass" x1="0" x2="1" y1="0" y2="0">
          <stop offset="0" stop-color="var(--bottle-dark)"/>
          <stop offset="0.35" stop-color="#1a0306"/>
          <stop offset="0.5" stop-color="var(--bottle-glow)"/>
          <stop offset="0.65" stop-color="#1a0306"/>
          <stop offset="1" stop-color="var(--bottle-dark)"/>
        </linearGradient>
        <linearGradient id="capsule" x1="0" x2="1" y1="0" y2="0">
          <stop offset="0" stop-color="var(--capsule-dark)"/>
          <stop offset="0.7" stop-color="var(--capsule-light)"/>
          <stop offset="1" stop-color="var(--capsule-dark)"/>
        </linearGradient>
      </defs>
      <path class="bottle__glass" fill="url(#glass)"
        d="M60,150 L60,170 C60,240 44,290 26,350 C12,396 5,425 5,470 L5,682 C5,700 11,712 20,720 C42,729 156,729 178,720 C187,712 193,700 193,682 L193,470 C193,425 186,396 172,350 C154,290 138,240 138,170 L138,150 Z"/>
      <path class="bottle__capsule" fill="url(#capsule)"
        d="M62,14 Q62,6 70,6 L128,6 Q136,6 136,14 L136,24 L138,24 Q141,24 141,28 L141,50 Q141,54 138,54 L138,155 L60,155 L60,54 Q57,54 57,50 L57,28 Q57,24 60,24 L62,24 Z"/>
      <rect x="62" y="24" width="74" height="2" fill="#5a5a5a"/>
      <rect x="60" y="52" width="78" height="2" fill="#5a5a5a"/>
      <rect class="bottle__capsule-band" x="60" y="150" width="78" height="4" fill="var(--capsule-band)"/>
    </svg>
    <section class="label">
      <div class="label__forest" role="img" aria-label="Engraved tree line of dark red firs over rolling hills"></div>
      <div class="label__frame"></div>
      <div class="label__mark"></div>
      <p class="label__winery">HARROWGATE<br>VINEYARDS</p>
      <p class="label__varietal">Syrah</p>
      <p class="label__vintage">2024</p>
      <p class="label__region">WILLAMETTE VALLEY</p>
    </section>
  </div>

  <p class="caption caption--label">Wine Label Design</p>
  <p class="caption caption--bottle">Sample on the bottle</p>

</main>
</body>
</html>
```